Flier for digital rights event targetting TMVA trade negotiators

We need a design for an event that my organization (a nonprofit) is hosting with academic experts, to address government negotiators who are taking part in the 19th round of negotiations of the Coastal Integrated Commerce Accord (TMVA). Unfortunately we don't have the exact details yet such as who the speakers are, what date the meeting is, or even what location it is, other than that it will be in Hyderabad, India. So you will need to make a design with placeholder values that we can swap out later. Here is some information about TMVA: https://en.examplepedia.org/wiki/Coastal_Integrated_Commerce_Accord. The event will be called: "An Expert Roundtable on Electronic Commerce and TMVA". I'm attaching some similar fliers for previous events.

Target Market(s)

Government trade ministries

Industry/Entity Type

Trade

Font styles to use
Serif
Sans Serif

Colors

Designer to choose colors to be used in the design.

Requirements
Must have
• Space for organizer logos, including LKB logo from https://www.lkbnet.org/press/logos
Nice to have
• Space for headshots of speakers (even though we haven't finalized who they are yet)
Should not have
• Cheesy stock graphics

```html
<!DOCTYPE html>
<html lang="en">
<head>
<meta charset="utf-8">
<title>An Expert Roundtable on Electronic Commerce and TMVA</title>
<link rel="stylesheet" href="https://fonts.googleapis.com/css2?family=Lato:ital,wght@0,300;0,400;0,700;1,400;1,700&display=swap">
<style>
  :root {
    --page: #ececec;
    --ink: #1c3024;
    --ink-soft: #2a2a2a;
    --banner-blue: #bcd9e8;
    --banner-grey: #d8d6d2;
    --frame: #5a6466;
    --photo-light: #d9d9d9;
    --photo-dark: #5a5a5a;
    --table: 47, 74, 76;
    --paper: #cfcbc5;
    --logo-red: #d0242b;
  }
  * { margin: 0; padding: 0; box-sizing: border-box; }
  html, body { width: 1200px; height: 1000px; overflow: hidden; }
  body { background: var(--page); font-family: "Lato", sans-serif; color: var(--ink); position: relative; }

  .flier {
    position: absolute; left: 86px; top: 313px; width: 1022px; height: 391px;
    border: 2px solid var(--frame);
    background: linear-gradient(100deg, var(--banner-blue) 0%, #ccdde3 30%, var(--banner-grey) 60%, #d6d3cf 100%);
    overflow: hidden;
  }
  .title {
    position: absolute; left: 25px; top: 11px;
    font-weight: 700; font-size: 66px; line-height: 1; letter-spacing: -0.4px; color: var(--ink);
  }
  .subtitle {
    position: absolute; left: 26px; top: 78px;
    font-weight: 300; font-size: 36px; line-height: 1; color: var(--ink);
  }
  .accord-name {
    position: absolute; left: 29px; top: 114px;
    font-style: italic; font-weight: 400; font-size: 21px; color: var(--ink);
  }
  .speaker { position: absolute; top: 157px; width: 110px; text-align: center; }
  .speaker-one { left: 29px; }
  .speaker-two { left: 158px; }
  .headshot {
    width: 110px; height: 135px; border: 1px solid #333;
    box-shadow: 2px 3px 6px rgba(0,0,0,.35);
  }
  .speaker-one .headshot { background: linear-gradient(180deg, var(--photo-light), #b5b5b5); }
  .speaker-two .headshot { background: linear-gradient(180deg, #8a8a8a, var(--photo-dark)); }
  .speaker-name { margin-top: 10px; font-style: italic; font-size: 16px; color: var(--ink-soft); white-space: nowrap; }

  .details { position: absolute; left: 311px; top: 156px; font-size: 17px; line-height: 1.3; color: var(--ink-soft); }
  .details dt { font-style: italic; font-weight: 700; color: var(--ink); }
  .details .rsvp { margin-top: 16px; }

  .organizer { position: absolute; left: 30px; top: 336px; display: flex; align-items: center; gap: 8px; }
  .organizer-dot { width: 22px; height: 22px; border-radius: 50%; background: var(--logo-red); }
  .organizer-name { font-weight: 700; font-size: 18px; color: var(--ink); }

  .roundtable-art {
    position: absolute; left: 650px; top: 8px; width: 370px; height: 375px;
    background:
      radial-gradient(circle at 50% 50%, rgba(var(--table), .55) 0%, rgba(var(--table), .4) 40%, rgba(var(--table), .12) 62%, rgba(var(--table), 0) 74%);
  }
</style>
</head>
<body>
  <section class="flier">
    <h1 class="title">An Expert Roundtable</h1>
    <p class="subtitle">on Electronic Commerce and TMVA</p>
    <p class="accord-name">Coastal Integrated Commerce Accord</p>

    <figure class="speaker speaker-one">
      <div class="headshot" role="img" aria-label="Headshot of speaker Daniel Marsh"></div>
      <figcaption class="speaker-name">Daniel Marsh</figcaption>
    </figure>
    <figure class="speaker speaker-two">
      <div class="headshot" role="img" aria-label="Headshot of speaker Victor Lanning"></div>
      <figcaption class="speaker-name">Victor Lanning</figcaption>
    </figure>

    <dl class="details">
      <dt>Date and Place:</dt>
      <dd>01 06 2017 &nbsp;|&nbsp; Hyderabad, India</dd>
      <dt>Venue:</dt>
      <dt class="rsvp">RSVP:</dt>
    </dl>

    <div class="organizer">
      <span class="organizer-dot"></span>
      <span class="organizer-name">LKB</span>
    </div>

    <div class="roundtable-art" role="img" aria-label="Illustration of negotiators seated around a round table with laptops, seen from above"></div>
  </section>
</body>
</html>
```